Property Maintenance company needs a noticeable Car Wrap design

We need an outstanding car wrap design for our Corvane Tessel Cargolite 2020. It needs to emphasize that our property maintenance company serves both Commercial and Residential clients. The wrap should communicate friendliness and quality services. I have attached a pdf file that outlines all the requirements for the wrap design. I also attached all relevant pictures to help with the creation of the design. The selected winner will receive the source files of the company logo & QTR logo to use in the car wrap design. I look forward to seeing all your designs!

Thank you!

Target Market(s)

Property Maintenance
Residential homeowners
Building owners

Industry/Entity Type

Property Maintenance

Requirements
Must have
• See Instruction file for all details.
Nice to have
• Some small icons that represent electrical, plumbing, handyman, and carpentry work.
For example, like a lightbulb, plug, or pipe icon. Or all of them. Try to use intuitive icons so the general public will know what it is.

Thanks!

```html
<!DOCTYPE html>
<html lang="en">
<head>
<meta charset="utf-8">
<title>Tallbrook Maintenance Services – Vehicle Wrap</title>
<link href="https://fonts.googleapis.com/css2?family=Poppins:wght@500;600;700&family=Oswald:wght@500&display=swap" rel="stylesheet">
<style>
  :root{
    --page:#f3f4f7;
    --panel:#ffffff;
    --panel-edge:#d9dce4;
    --blue:#4a74d8;
    --navy:#1d2f7a;
    --green:#6cc04a;
    --white:#ffffff;
    --badge:#2f5fb3;
  }
  html,body{margin:0;padding:0;overflow:hidden;background:var(--page);}
  .wrap-canvas{display:block;width:1200px;height:1200px;}
  .panel{fill:var(--panel);stroke:var(--panel-edge);stroke-width:2;}
  .band-blue{fill:var(--blue);}
  .band-green{fill:var(--green);}
  .badge{fill:var(--badge);}
  .icon-disc{fill:var(--white);}
  .icon-line{fill:none;stroke:var(--blue);stroke-width:4;stroke-linecap:round;stroke-linejoin:round;}
  .logo-mark{fill:none;stroke:var(--navy);stroke-width:4;}
  .logo-name{font-family:'Poppins',sans-serif;font-weight:600;fill:var(--navy);letter-spacing:1px;}
  .logo-sub{font-family:'Poppins',sans-serif;font-weight:500;fill:var(--blue);letter-spacing:4px;}
  .service-list{font-family:'Oswald',sans-serif;font-weight:500;fill:var(--navy);font-size:13px;}
  .web{font-family:'Poppins',sans-serif;font-weight:500;fill:var(--white);}
  .phone{font-family:'Poppins',sans-serif;font-weight:700;fill:var(--white);}
  .tagline{font-family:'Poppins',sans-serif;font-weight:600;fill:var(--green);letter-spacing:.5px;}
  .headline{font-family:'Poppins',sans-serif;font-weight:700;fill:var(--navy);letter-spacing:3px;}
  .more{font-family:'Poppins',sans-serif;font-weight:600;fill:var(--white);}
  .rear .web,.rear .phone{fill:var(--navy);}
  .rear .tagline{fill:var(--blue);letter-spacing:0;}
  .rear .more{fill:var(--navy);}
  .front-web{font-family:'Poppins',sans-serif;font-weight:700;fill:var(--white);}
</style>
</head>
<body>
<svg class="wrap-canvas" viewBox="0 0 1200 1200" xmlns="http://www.w3.org/2000/svg">
  <defs>
    <g id="icon-tools">
      <path class="icon-line" d="M-12 -12 L12 12 M12 -12 L-12 12 M-16 -8 L-8 -16 M8 16 L16 8"/>
    </g>
    <g id="icon-hammer">
      <path class="icon-line" d="M-12 12 L8 -8 M2 -14 L14 -2 M-12 -12 L12 12"/>
    </g>
    <g id="icon-pipe">
      <path class="icon-line" d="M-10 -14 L-10 4 Q-10 14 0 14 Q10 14 10 4 L10 -6 M-14 -14 L-6 -14 M6 -6 L14 -6"/>
    </g>
    <g id="icon-plug">
      <path class="icon-line" d="M-10 -6 L10 -6 L10 2 Q10 10 0 10 Q-10 10 -10 2 Z M-5 -6 L-5 -14 M5 -6 L5 -14 M0 10 L0 17"/>
    </g>
    <g id="icon-house">
      <path class="icon-line" d="M-14 0 L0 -13 L14 0 M-9 -4 L-9 13 L9 13 L9 -4 M-3 13 L-3 4 L3 4 L3 13"/>
    </g>
  </defs>

  <!-- Side panel -->
  <g class="side">
    <rect class="panel" x="40" y="90" width="1120" height="460" rx="40"/>
    <polygon class="band-green" points="40,316 1160,296 1160,304 40,324"/>
    <polygon class="band-blue" points="40,330 1160,310 1160,372 620,382 320,398 40,404"/>

    <g class="logo" transform="translate(868,215)">
      <rect class="logo-mark" x="0" y="-36" width="40" height="40"/>
      <text class="logo-name" x="52" y="0" font-size="32">TALLBROOK</text>
      <text class="logo-sub" x="54" y="26" font-size="11">MAINTENANCE SERVICES</text>
    </g>

    <text class="service-list" x="616" y="203">• MAINTENANCE PACKAGES.</text>
    <text class="service-list" x="616" y="221">• GENERAL MAINTENANCE/HANDYMAN REPAIRS</text>
    <text class="service-list" x="616" y="239">• SPECIAL PROJECTS &amp; RENOVATIONS</text>

    <rect class="badge" x="216" y="345" width="34" height="44" rx="4" role="img" aria-label="QTR accreditation badge"/>

    <text class="web" x="348" y="352" font-size="20">www.tallbrookfs.com</text>
    <text class="phone" x="346" y="382" font-size="29">403-555-0142</text>
    <text class="tagline" x="352" y="412" font-size="13">PROPERTY MAINTENANCE SERVICES</text>
    <text class="headline" x="357" y="476" font-size="30">COMMERCIAL &amp; RESIDENTIAL</text>

    <g transform="translate(678,354)"><circle class="icon-disc" r="28"/><use href="#icon-tools"/></g>
    <g transform="translate(756,353)"><circle class="icon-disc" r="28"/><use href="#icon-hammer"/></g>
    <g transform="translate(834,352)"><circle class="icon-disc" r="28"/><use href="#icon-pipe"/></g>
    <g transform="translate(912,351)"><circle class="icon-disc" r="28"/><use href="#icon-plug"/></g>
    <g transform="translate(990,349)"><circle class="icon-disc" r="28"/><use href="#icon-house"/></g>
    <text class="more" x="1045" y="340" font-size="12">AND MUCH</text>
    <text class="more" x="1045" y="356" font-size="12">MORE</text>
  </g>

  <!-- Rear panel -->
  <g class="rear">
    <rect class="panel" x="150" y="690" width="380" height="440" rx="30"/>
    <text class="headline" x="340" y="735" font-size="14" text-anchor="middle" letter-spacing="1">COMMERCIAL &amp; RESIDENTIAL</text>
    <g class="logo" transform="translate(218,800)">
      <rect class="logo-mark" x="0" y="-30" width="32" height="32"/>
      <text class="logo-name" x="42" y="0" font-size="28">TALLBROOK</text>
      <text class="logo-sub" x="44" y="22" font-size="10">MAINTENANCE SERVICES</text>
    </g>
    <rect class="band-blue" x="150" y="840" width="380" height="52"/>
    <rect class="band-green" x="150" y="892" width="380" height="7"/>
    <g transform="translate(193,866)"><circle class="icon-disc" r="21"/><use href="#icon-tools" transform="scale(.75)"/></g>
    <g transform="translate(252,866)"><circle class="icon-disc" r="21"/><use href="#icon-hammer" transform="scale(.75)"/></g>
    <g transform="translate(311,866)"><circle class="icon-disc" r="21"/><use href="#icon-pipe" transform="scale(.75)"/></g>
    <g transform="translate(370,866)"><circle class="icon-disc" r="21"/><use href="#icon-plug" transform="scale(.75)"/></g>
    <g transform="translate(429,866)"><circle class="icon-disc" r="21"/><use href="#icon-house" transform="scale(.75)"/></g>
    <text class="more" x="460" y="862" font-size="10">AND MUCH</text>
    <text class="more" x="460" y="875" font-size="10">MORE</text>
    <rect class="badge" x="466" y="910" width="28" height="36" rx="3" role="img" aria-label="QTR accreditation badge"/>
    <text class="web" x="188" y="982" font-size="15">www.tallbrookfs.com</text>
    <text class="phone" x="186" y="1010" font-size="22">403-555-0142</text>
    <text class="tagline" x="366" y="997" font-size="7.5">PROPERTY MAINTENANCE SERVICES</text>
  </g>

  <!-- Front panel -->
  <g class="front">
    <rect class="panel" x="630" y="850" width="440" height="170" rx="30"/>
    <g class="logo" transform="translate(752,892)">
      <rect class="logo-mark" x="0" y="-20" width="22" height="22" style="stroke-width:3"/>
      <text class="logo-name" x="30" y="0" font-size="19">TALLBROOK</text>
      <text class="logo-sub" x="31" y="14" font-size="7">MAINTENANCE SERVICES</text>
    </g>
    <polygon class="band-blue" points="630,925 730,925 750,1020 660,1020 630,990"/>
    <polygon class="band-blue" points="1070,925 970,925 950,1020 1040,1020 1070,990"/>
    <rect class="band-green" x="745" y="920" width="210" height="26" rx="4"/>
    <text class="front-web" x="850" y="939" font-size="15" text-anchor="middle">www.tallbrookfs.com</text>
  </g>
</svg>
</body>
</html>
```